Cover für Buch zu den Themen Geschichte, Ethnologie, Soziologie
Hallo Herr Wendel, das sieht alles sehr gut aus - vielen Dank Ihnen! Ich freue mich, dass Sie hier mit dem richtigen Gespür für das Buch und die optische Wirkung ein so ansprechendes Cover gestaltet haben! Sollte beim Hochladen bei KfV noch ein Problem auftreten, würde ich mich bei Ihnen nochmal melden, ansonsten kann das alles so veröffentlicht werden. In diesem Sinne: Viele Grüße und Ihnen eine gute Woche! Jonas Riedl
Zielgruppe
Zielgruppe: Interessierte an Geschichte, Ethnologie, Soziologie
Aufgabenstellung
Hauptbildelement soll ein Motiv zu „Familie“ sein, gern auch etwas (aber nicht zu sehr) abstrahiert.
Klare - gut lesbare Schriftzüge.

```html
<!DOCTYPE html>
<html lang="de">
<head>
<meta charset="utf-8">
<title>Enthaltung und Zivilisation – Buchcover</title>
<link rel="stylesheet" href="https://fonts.googleapis.com/css2?family=Saira:wght@300;600;700&family=PT+Sans:ital,wght@0,400;1,400&display=swap">
<style>
  :root {
    --canvas-bg: #f1f1f1;
    --paper: #f5f0ed;
    --title-coral: #d97a5f;
    --band-rust: #cc5f3e;
    --ink: #2b2b2b;
    --ink-soft: #3c3c3c;
    --white: #ffffff;
    --figure-light: #f3b59c;
    --figure-mid: #ec8d6c;
    --figure-deep: #d56a48;
  }
  * { margin: 0; padding: 0; box-sizing: border-box; }
  html, body { width: 1200px; height: 800px; overflow: hidden; }
  body {
    background: var(--canvas-bg);
    display: flex;
    align-items: center;
    justify-content: center;
    gap: 30px;
  }
  .cover {
    width: 400px;
    height: 590px;
    background: var(--paper);
    position: relative;
    overflow: hidden;
    box-shadow: 0 10px 30px rgba(0,0,0,0.12);
  }

  /* Back cover */
  .back-cover { font-family: "PT Sans", sans-serif; color: var(--ink); }
  .back-header { padding: 52px 44px 0; }
  .back-author { font-size: 14px; }
  .back-title { font-size: 19px; font-weight: 400; margin-top: 6px; }
  .back-body {
    padding: 36px 44px 0;
    font-size: 12.3px;
    line-height: 1.6;
    color: var(--ink-soft);
    text-align: justify;
    hyphens: auto;
  }
  .back-body p + p { margin-top: 16px; }
  .back-band {
    position: absolute;
    left: 0; right: 0; bottom: 0;
    height: 110px;
    background: var(--band-rust);
    padding: 20px 44px;
  }
  .back-quote {
    font-style: italic;
    font-size: 12px;
    line-height: 1.5;
    color: var(--white);
  }

  /* Front cover */
  .front-cover { font-family: "Saira", sans-serif; }
  .front-author {
    text-align: center;
    font-weight: 300;
    font-size: 25px;
    color: var(--ink-soft);
    margin-top: 52px;
  }
  .front-title {
    text-align: center;
    font-weight: 700;
    font-size: 44px;
    line-height: 1.0;
    letter-spacing: 0.5px;
    color: var(--title-coral);
    text-transform: uppercase;
    margin-top: 6px;
  }
  .family-motif {
    position: absolute;
    left: 0; right: 0;
    top: 190px;
    height: 300px;
    display: block;
  }
  .front-band {
    position: absolute;
    left: 0; right: 0; bottom: 0;
    height: 112px;
    background: var(--band-rust);
    display: flex;
    align-items: center;
    justify-content: center;
  }
  .front-subtitle {
    text-align: center;
    color: var(--white);
    font-weight: 600;
    font-size: 17px;
    line-height: 1.2;
  }
</style>
</head>
<body>

  <section class="cover back-cover" aria-label="Buchrückseite">
    <header class="back-header">
      <p class="back-author">Jakob D. Umland</p>
      <h2 class="back-title">Enthaltung und Zivilisation</h2>
    </header>
    <div class="back-body">
      <p>In seiner umfangreichen Untersuchung „Custom and Culture“ fragte der britische Ethnologe, wie eng die Regeln des Zusammenlebens mit der Entwicklung ganzer Gemeinschaften verbunden sind. Dafür wertete er eine Vielzahl ethnologischer und historischer Quellen aus. Seine Befunde regen bis heute zur Diskussion an: Er beschreibt, wie stark Blüte und Wandel von Kulturen davon abhängen, welchen Rang Ehe, Verantwortung und Familie einnehmen. Gemeinschaften, die verbindliche Formen des Zusammenlebens aufgaben, verloren nach seiner Deutung an Kraft.</p>
      <p>Die vorliegende Ausgabe bietet erstmals eine deutschsprachige Auswahl aus „Custom and Culture“, die alle für Leserinnen und Leser zentralen Kapitel sowie – in ausgewählten Auszügen – die ethnologischen Belege umfasst.</p>
    </div>
    <div class="back-band">
      <p class="back-quote">„Ein zugleich origineller wie besonnener Geist. … Ein Werk von großer Tragweite. Umland stützt seine Thesen auf eine beeindruckende Fülle an Material.“<br>(Edwin Harlow)</p>
    </div>
  </section>

  <section class="cover front-cover" aria-label="Buchvorderseite">
    <p class="front-author">Jakob D. Umland</p>
    <h1 class="front-title">Enthaltung und<br>Zivilisation</h1>
    <svg class="family-motif" viewBox="0 0 400 300" preserveAspectRatio="none" role="img" aria-label="Abstrahierte Illustration einer sich umarmenden Gruppe von Menschen in Apricot- und Rosttönen">
      <defs>
        <linearGradient id="motifTones" x1="0" y1="0" x2="1" y2="0">
          <stop offset="0" stop-color="var(--figure-light)"/>
          <stop offset="0.45" stop-color="var(--figure-mid)"/>
          <stop offset="0.7" stop-color="var(--figure-deep)"/>
          <stop offset="1" stop-color="var(--figure-light)"/>
        </linearGradient>
      </defs>
      <rect x="0" y="0" width="400" height="300" fill="url(#motifTones)"/>
    </svg>
    <div class="front-band">
      <p class="front-subtitle">Wie feste Bindungen<br>Kulturen und Gemeinschaften<br>langfristig tragen</p>
    </div>
  </section>

</body>
</html>
```